Marlow Family Chiropractic Stationary

The letterhead and business card must have our logo.
We would like to see the logo used in different ways ( It can be expanded upon in the stationary.)
Please use the the same or similar colors.
Must be eye catching and memorable.
Must be easy to read

Reason: The doctor has been too busy to make any final decisions. He would like to give himself a little more time.

Target Market(s)

Chiropractic Healthcare

Industry/Entity Type

Business

Requirements
Must have
• Dr. Nathaniel Marlow D.C.
Chiropractor

802-555-0193

415 Birchwood Parkway, 2nd Floor
Ashbury, VT 05499

drmarlow@marlowspine.example
www.marlowspine.example
www.facebook.com/MarlowFamilySpine
Should not have
• should not be difficult to read

```html
<!DOCTYPE html>
<html lang="en">
<head>
<meta charset="utf-8">
<title>Marlow Family Chiropractic – Business Card</title>
<link href="https://fonts.googleapis.com/css2?family=Questrial&family=Nunito:wght@800&display=swap" rel="stylesheet">
<style>
  :root {
    --card-green: #2a9a4a;
    --name-white: #ffffff;
    --contact-yellow: #f7ec1c;
  }
  html, body {
    margin: 0;
    padding: 0;
    overflow: hidden;
    background: var(--card-green);
  }
  .business-card {
    position: relative;
    width: 1200px;
    height: 667px;
    background: var(--card-green);
    overflow: hidden;
  }
  .doctor-name {
    position: absolute;
    left: 68px;
    top: 96px;
    margin: 0;
    font-family: "Questrial", sans-serif;
    font-weight: 400;
    font-size: 49px;
    line-height: 1;
    letter-spacing: 0.6px;
    white-space: nowrap;
    color: var(--name-white);
    -webkit-text-stroke: 1.1px var(--name-white);
  }
  .doctor-title {
    position: absolute;
    left: 69px;
    top: 152px;
    margin: 0;
    font-family: "Questrial", sans-serif;
    font-size: 24px;
    line-height: 1;
    letter-spacing: 41.5px;
    white-space: nowrap;
    color: var(--name-white);
    -webkit-text-stroke: 0.6px var(--name-white);
  }
  .contact-list {
    position: absolute;
    left: 68px;
    top: 411px;
    margin: 0;
    padding: 0;
    list-style: none;
    font-family: "Nunito", sans-serif;
    font-weight: 800;
    font-size: 29px;
    line-height: 33.2px;
    white-space: nowrap;
    color: var(--contact-yellow);
  }
  .practice-mark {
    position: absolute;
    right: 60px;
    bottom: 90px;
    display: flex;
    align-items: center;
    gap: 18px;
    font-family: "Nunito", sans-serif;
    font-weight: 800;
    font-size: 30px;
    line-height: 1.15;
    color: var(--name-white);
  }
  .practice-mark__dot {
    width: 46px;
    height: 46px;
    border-radius: 50%;
    background: var(--name-white);
    flex: none;
  }
</style>
</head>
<body>
  <div class="business-card">
    <h1 class="doctor-name">Dr. Nathaniel Marlow D.C.</h1>
    <p class="doctor-title">Chiropractor</p>

    <ul class="contact-list">
      <li>802-555-0193</li>
      <li>415 Birchwood Parkway, 2nd Floor</li>
      <li>Ashbury, VT 05499</li>
      <li>drmarlow@marlowspine.example</li>
      <li>www.marlowspine.example</li>
      <li>www.facebook.com/MarlowFamilySpine</li>
    </ul>

    <div class="practice-mark">
      <span class="practice-mark__dot"></span>
      <span class="practice-mark__name">Marlow Family<br>Chiropractic</span>
    </div>
  </div>
</body>
</html>
```